Halworth Builds, Carpentry Services

Business card for carpentry business in the Sunshine Coast.

Business card layout required using logo provided - provided both PDF copy and AI. Please let me know if you would like a the files for the logo symbol and text by itself.

Business Colours are grey, blue and white. The font colours codes for this design are Blue Hex # 00B4E6 and Hex # 39393B for the gray colour.

FYI font for logo is Gotham Bold.

Preference for a clean and striking layout that is simple and elegant.

Target Market(s)

Young Families, retirees, young couples requiring assistance with small to medium works/renovations on the Sunshine Coast.

Industry/Entity Type

Construction

Contact Information for Business Card

Dean Halworth
Carpenter
0481356027
dean@halworthbuilds.com.au
Wyndell Heads, Coral Coast
RHLA Licensed Carpenter (In smaller font)

Font styles to use
Sans Serif

Colors

Designer to choose colors to be used in the design.

Requirements
Must have
• Logo provided must appear on the card, preferably on one side of the card by itself with the text on the alternate side
Nice to have
• Text on the other side of card, maybe grey background and white font here but happy for the designer to provide ideas here.
Should not have
• Use of other colours, other than the ones provided - white, grey and blue. Black optional.

```html
<!DOCTYPE html>
<html lang="en">
<head>
<meta charset="utf-8">
<title>Halworth Builds – Business Card</title>
<link rel="stylesheet" href="https://fonts.googleapis.com/css2?family=Montserrat:wght@400;500;700&display=swap">
<style>
  :root {
    --blue: #00B4E6;
    --grey: #39393B;
    --card-dark: #333335;
    --white: #ffffff;
    --backdrop: #1c1c1d;
  }
  * { box-sizing: border-box; margin: 0; padding: 0; }
  html, body {
    width: 1200px; height: 900px; overflow: hidden;
    background: var(--backdrop);
    font-family: "Montserrat", Arial, sans-serif;
  }
  .canvas { position: relative; width: 1200px; height: 900px; }
  .card {
    position: absolute; left: 290px; width: 620px; height: 354px;
    overflow: hidden;
    box-shadow: 0 12px 30px rgba(0,0,0,.45);
  }
  .card--front { top: 70px; background: var(--card-dark); }
  .card--back { top: 476px; background: var(--white); }

  /* front */
  .lockup {
    position: absolute; left: 140px; top: 128px;
    display: flex; align-items: center; gap: 20px;
  }
  .lockup__mark { width: 64px; height: 64px; background: var(--blue); flex: none; }
  .lockup__divider { width: 2px; height: 86px; background: var(--blue); flex: none; }
  .lockup__text { width: 230px; }
  .lockup__name {
    font-weight: 700; font-size: 34px; letter-spacing: 1.5px;
    color: var(--blue); text-transform: uppercase; line-height: 1;
  }
  .lockup__tagline {
    display: flex; align-items: center; gap: 8px; margin-top: 12px;
    color: var(--white); font-size: 9px; letter-spacing: 2.5px; text-transform: uppercase;
    white-space: nowrap;
  }
  .lockup__tagline::before, .lockup__tagline::after {
    content: ""; flex: 1; height: 1px; background: var(--white);
  }

  /* back */
  .brand {
    position: absolute; left: 48px; top: 118px; width: 190px;
    display: flex; flex-direction: column; align-items: flex-start; gap: 12px;
  }
  .brand__mark { width: 54px; height: 54px; background: var(--blue); }
  .brand__name {
    font-weight: 700; font-size: 22px; color: var(--blue);
    text-transform: uppercase; letter-spacing: 1px; line-height: 1.1;
  }
  .divider { position: absolute; left: 262px; top: 104px; width: 2px; height: 150px; background: var(--blue); }
  .contact { position: absolute; left: 284px; top: 104px; color: var(--grey); }
  .contact__name {
    font-weight: 700; font-size: 26px; color: var(--blue);
    text-transform: uppercase; letter-spacing: 1px; line-height: 1;
  }
  .contact__role { font-size: 17px; margin-top: 4px; }
  .contact__list { list-style: none; margin-top: 22px; font-size: 17px; line-height: 1.45; }
  .contact__list li { display: flex; align-items: center; gap: 10px; }
  .contact__list svg { width: 16px; height: 16px; flex: none; }
  .licence {
    position: absolute; left: 0; right: 0; bottom: 30px;
    text-align: center; font-size: 14px; color: var(--grey);
  }
</style>
</head>
<body>
<main class="canvas">
  <section class="card card--front" aria-label="Card front">
    <div class="lockup">
      <div class="lockup__mark"></div>
      <div class="lockup__divider"></div>
      <div class="lockup__text">
        <p class="lockup__name">Halworth Builds</p>
        <p class="lockup__tagline">Carpentry Services</p>
      </div>
    </div>
  </section>

  <section class="card card--back" aria-label="Card back">
    <div class="brand">
      <div class="brand__mark"></div>
      <p class="brand__name">Halworth Builds</p>
    </div>
    <div class="divider"></div>
    <div class="contact">
      <p class="contact__name">Dean Halworth</p>
      <p class="contact__role">Carpenter</p>
      <ul class="contact__list">
        <li>
          <svg viewBox="0 0 16 16" fill="none" stroke="var(--blue)" stroke-width="1.3"><circle cx="8" cy="8" r="7"/><path d="M5.5 4.5l1.4 1.6-.8 1.1c.5 1.1 1.4 2 2.5 2.5l1.1-.8 1.6 1.4-.9 1.1c-2.6-.3-5-2.7-5.3-5.3z"/></svg>
          0481 356 027
        </li>
        <li>
          <svg viewBox="0 0 16 16" fill="none" stroke="var(--blue)" stroke-width="1.3"><rect x="1.5" y="3.5" width="13" height="9"/><path d="M1.5 3.5L8 9l6.5-5.5"/></svg>
          dean@halworthbuilds.com.au
        </li>
        <li>
          <svg viewBox="0 0 16 16" fill="var(--blue)"><path d="M8 1.5L1 8h2v6.5h4v-4h2v4h4V8h2z"/></svg>
          Wyndell Heads, Coral Coast
        </li>
      </ul>
    </div>
    <p class="licence">RHLA Licensed Carpenter</p>
  </section>
</main>
</body>
</html>
```